UPDATE: I have uploaded the selected logo from the other contest, please use it in your designs.

I have a logo design contest as well so not sure how PixelGuild handles that. They should integrate at some point. I will describe the overall theme with the logo description. See it for details.

The business card side of it would just build on that same theme.

Target Market(s)

8-40

Industry/Entity Type

Business

Contact Information for Business Card

FirstName LastName
Email

Logo Text

Velimor

Font styles to use
Sans Serif

Requirements
Must have
• the url Velimor.com somewhere in it.

```html
<!DOCTYPE html>
<html lang="en">
<head>
<meta charset="utf-8">
<title>Velimor Business Card</title>
<link rel="stylesheet" href="https://fonts.googleapis.com/css2?family=Michroma&display=swap">
<style>
  :root {
    --backdrop: #9a9a9a;
    --card: #ffffff;
    --brand-green: #8cc63f;
    --brand-blue: #1b75bc;
    --ink-white: #ffffff;
  }
  html, body {
    margin: 0;
    width: 1200px;
    height: 900px;
    overflow: hidden;
    background: var(--backdrop);
    font-family: "Michroma", sans-serif;
  }
  .stage {
    width: 1200px;
    height: 900px;
    display: flex;
    flex-direction: column;
    align-items: center;
    justify-content: center;
    gap: 40px;
  }
  .card {
    position: relative;
    width: 700px;
    height: 400px;
    background: var(--card);
    box-shadow: 0 6px 18px rgba(0,0,0,0.25);
  }
  .contact-band {
    position: absolute;
    left: 0;
    top: 140px;
    width: 390px;
    height: 70px;
    background: var(--brand-green);
    display: flex;
    flex-direction: column;
    justify-content: center;
    align-items: center;
    gap: 6px;
    color: var(--ink-white);
    letter-spacing: 0.14em;
    font-size: 13px;
  }
  .contact-band .person-name { text-transform: capitalize; }
  .contact-band .person-email { text-transform: lowercase; }
  .back-brand {
    position: absolute;
    left: 430px;
    top: 140px;
    width: 240px;
    display: flex;
    flex-direction: column;
    align-items: center;
  }
  .brand-lockup {
    display: flex;
    align-items: center;
    gap: 10px;
  }
  .brand-mark {
    border-radius: 50%;
    background: var(--brand-green);
  }
  .brand-name {
    color: var(--brand-blue);
    text-transform: uppercase;
    letter-spacing: 0.08em;
  }
  .back-brand .brand-mark { width: 22px; height: 22px; }
  .back-brand .brand-name { font-size: 26px; }
  .brand-url {
    margin-top: 4px;
    color: var(--brand-blue);
    font-size: 11px;
    letter-spacing: 0.12em;
    text-transform: uppercase;
  }
  .card-front {
    display: flex;
    align-items: center;
    justify-content: center;
  }
  .card-front .brand-mark { width: 52px; height: 52px; }
  .card-front .brand-name { font-size: 58px; letter-spacing: 0.12em; }
</style>
</head>
<body>
  <main class="stage">
    <section class="card card-back">
      <div class="contact-band">
        <span class="person-name">Jordan Hale</span>
        <span class="person-email">jordan@velimor.com</span>
      </div>
      <div class="back-brand">
        <div class="brand-lockup">
          <span class="brand-mark"></span>
          <span class="brand-name">Velimor</span>
        </div>
        <span class="brand-url">www.Velimor.com</span>
      </div>
    </section>
    <section class="card card-front">
      <div class="brand-lockup">
        <span class="brand-mark"></span>
        <span class="brand-name">Velimor</span>
      </div>
    </section>
  </main>
</body>
</html>
```